Book cover for book entitled "Sweeping the Porch at Dawn ....and Keeping It Bright All Season Long"

I need a book cover for ebook and 6" x 9" paperback print book (brook press pod). I want a simple but "positive" cover with no gothic or darkness in design. I would prefer a "hopeful color scheme" in yellow, blue, green analogous colors and very easy to read main title "Sweeping the Porch at Dawn". I want the tag line of the title. "and keep it bright all season long" included on the cover please. I am not opposed to white in the color scheme I believe the graphic needs to somehow deal with doors, blocks, keys (perhaps a combination lock since the book is my story of healing from pancreatic cancer through faith, nutrition, and lifestyle changes). I am basically looking for the front cover from you but in a high definition format so it can be transferred to posters and banners for seminar displays. I am uploading my photo in case a designer would want to include a small copy of it in a design although I plan the photo to be on the back cover. The photo could, of course, be cropped.

I would also be interested in seeing a design with a woman  with arms folded and looking satisfied or victorious (happy) casually leaning against a closed door.    It can be very simple....

This graphic could be photo or drawing-even a good line drawing.   Almost whimsical would be okay.  This cover need not be highly complicated but I do want the title easy to read in small or large sizes for ebook and print book.

Reason: I have just changed to "committed" and some new "acceptances" have just come in.

Nutrition

Serif

fbee3e
acd037
33b7a4
34a6d8
3377b5

```html
<!DOCTYPE html>
<html lang="en">
<head>
<meta charset="utf-8">
<title>Sweeping the Porch at Dawn — Cover</title>
<link href="https://fonts.googleapis.com/css2?family=Oswald:wght@500;600&display=swap" rel="stylesheet">
<style>
  :root{
    --page-bg:#ececec;
    --door-light:#cfa878;
    --door-mid:#b98f62;
    --door-dark:#6a4a35;
    --hanger:#f4f4f2;
    --title-blue:#2f7fc4;
    --band-green:#7fbf3f;
    --band-text:#ffffff;
    --collage-light:#f5e6e4;
    --collage-mid:#e4c3bf;
  }
  *{margin:0;padding:0;box-sizing:border-box}
  html,body{width:1111px;height:1200px;overflow:hidden;background:var(--page-bg)}
  .canvas{position:relative;width:1111px;height:1200px}
  .cover{position:absolute;left:220px;top:40px;width:672px;height:1120px;overflow:hidden}
  .door-photo{
    position:absolute;inset:0;
    background:linear-gradient(90deg,var(--door-mid) 0%,var(--door-light) 45%,var(--door-mid) 88%,var(--door-dark) 90%,var(--door-dark) 100%);
  }
  .door-hanger{
    position:absolute;left:73px;top:117px;width:406px;height:851px;
    background:var(--hanger);border-radius:16px;overflow:hidden;
    box-shadow:0 3px 8px rgba(0,0,0,.18);
  }
  .knob-opening{
    position:absolute;left:46px;top:-20px;width:314px;height:314px;border-radius:50%;
    background:var(--door-light);
  }
  .title{
    position:absolute;left:0;top:360px;width:100%;text-align:center;
    font-family:'Oswald',sans-serif;font-weight:600;color:var(--title-blue);
    text-transform:uppercase;line-height:1;
  }
  .title span{display:block}
  .title .line-1{font-size:80px;letter-spacing:1px}
  .title .line-2,.title .line-3{font-size:56px;margin-top:6px}
  .word-collage{
    position:absolute;left:34px;top:590px;width:338px;height:210px;
    background:linear-gradient(135deg,var(--collage-light) 0%,var(--collage-mid) 50%,var(--collage-light) 100%);
  }
  .tagline-band{
    position:absolute;left:0;bottom:0;width:100%;height:46px;
    background:var(--band-green);color:var(--band-text);
    display:flex;align-items:center;justify-content:center;
    font-family:'Oswald',sans-serif;font-weight:500;font-size:21px;
    text-transform:uppercase;letter-spacing:.3px;white-space:nowrap;
  }
</style>
</head>
<body>
<div class="canvas">
  <div class="cover">
    <div class="door-photo" role="img" aria-label="Photo of a light wooden door with a brushed steel door knob"></div>
    <div class="door-hanger">
      <div class="knob-opening" role="img" aria-label="Door knob passing through the hanger opening"></div>
      <h1 class="title">
        <span class="line-1">Sweeping</span>
        <span class="line-2">The Porch</span>
        <span class="line-3">At Dawn</span>
      </h1>
      <div class="word-collage" role="img" aria-label="Word collage of health and healing terms on taped paper"></div>
      <div class="tagline-band">and keep it bright all season long</div>
    </div>
  </div>
</div>
</body>
</html>
```